Color palette UI design and CSS

I need a color palette design and the CSS implementation for the main UI components.
This is for a legal company and the concepts they want reflected are sophistication, elegance, minimalistic.
Attached is the company logo and an example of what you should deliver. In case of winning the contest you must implement the CSS.

```html
<!DOCTYPE html>
<html lang="en">
<head>
<meta charset="utf-8">
<title>Color Palette &amp; Buttons</title>
<link rel="stylesheet" href="https://fonts.googleapis.com/css2?family=Lato:wght@400;700&display=swap">
<style>
  :root {
    --primary-dark: #1f4e6e;
    --primary: #2a7fb5;
    --primary-light: #7fb1d6;
    --secondary: #72c7c4;
    --secondary-light: #cdeee9;
    --accent: #52275e;
    --accent-light: #b07cc6;
    --tone-charcoal: #454545;
    --tone-slate: #34434f;
    --ink: #222222;
    --paper: #ffffff;
  }
  * { box-sizing: border-box; margin: 0; padding: 0; }
  html, body { width: 1200px; height: 1041px; overflow: hidden; background: var(--paper); }
  body { position: relative; font-family: "Lato", sans-serif; color: var(--ink); }

  .abs { position: absolute; }
  .heading-xl { font-size: 27px; font-weight: 400; line-height: 1; }
  .heading-md { font-size: 20px; font-weight: 400; line-height: 1; }

  .swatch { position: absolute; top: 96px; width: 56px; height: 56px; border-radius: 50%; }

  .btn {
    position: absolute; display: flex; align-items: center; justify-content: center; gap: 5px;
    border-radius: 2px; font-family: "Lato", sans-serif; white-space: nowrap;
  }
  .btn svg { flex: none; }
  .btn-icon { width: 107px; height: 32px; font-size: 13px; }
  .btn-chevron { width: 139px; height: 39px; font-size: 17px; }
  .btn-large { width: 124px; height: 40px; font-size: 17px; }

  .solid-primary { background: var(--primary-dark); color: #fff; fill: #fff; }
  .solid-secondary { background: var(--secondary); color: #eaf8f7; fill: #fff; }
  .solid-accent { background: var(--accent); color: #fff; fill: #fff; }

  .outline-primary { border: 1.5px solid var(--primary-dark); color: var(--primary-dark); fill: var(--primary-dark); }
  .outline-secondary { border: 1.5px solid var(--secondary); color: var(--secondary); fill: var(--secondary); }
  .outline-accent { border: 1.5px solid var(--accent); color: #4a3a50; fill: var(--accent); }

  .text-btn { position: absolute; display: flex; align-items: center; gap: 4px; font-size: 13px; font-weight: 700; line-height: 1; }
  .text-primary { color: var(--primary-dark); fill: var(--primary-dark); }
  .text-secondary { color: var(--secondary); fill: var(--secondary); }
  .text-accent { color: var(--accent); fill: var(--accent); }

  .group-btn { position: absolute; top: 803px; height: 32px; display: flex; align-items: center; justify-content: center; font-size: 13px; border-radius: 2px; }

  .icon-round { position: absolute; top: 803px; width: 32px; height: 32px; border-radius: 50%; background: var(--primary-dark); display: flex; align-items: center; justify-content: center; }
  .chip { position: absolute; left: 612px; top: 840px; width: 76px; height: 32px; border-radius: 16px; background: var(--primary-dark); color: #fff; font-size: 13px; display: flex; align-items: center; justify-content: center; gap: 9px; }

  .form-row { position: absolute; left: 137px; display: flex; align-items: center; gap: 8px; font-size: 13px; color: #444; line-height: 1; }
  .radio { width: 13px; height: 13px; border-radius: 50%; }
  .radio.on { border: 4px solid var(--primary-dark); }
  .radio.off { border: 1px solid #ccc; }
  .checkbox { width: 13px; height: 13px; border-radius: 2px; background: var(--primary-dark); display: flex; align-items: center; justify-content: center; }
  .toggle { position: absolute; left: 137px; top: 993px; width: 50px; height: 29px; border-radius: 15px; background: var(--primary-dark); }
  .toggle::after { content: ""; position: absolute; right: 4px; top: 4px; width: 21px; height: 21px; border-radius: 50%; background: #fff; }
</style>
</head>
<body>
  <svg width="0" height="0" style="position:absolute">
    <defs>
      <symbol id="heart" viewBox="0 0 24 24"><path d="M12 21.5 10.5 20C5 15 1.5 11.9 1.5 8A5.4 5.4 0 0 1 7 2.5c1.9 0 3.7.9 5 2.3a6.6 6.6 0 0 1 5-2.3A5.4 5.4 0 0 1 22.5 8c0 3.9-3.5 7-9 12z"/></symbol>
      <symbol id="chevron" viewBox="0 0 24 24"><path d="M7 3.5 9.6 1l11 11-11 11L7 20.5l8.5-8.5z"/></symbol>
    </defs>
  </svg>

  <!-- Colour palette -->
  <h1 class="abs heading-xl" style="left:137px; top:24px;">Color Palette</h1>

  <section class="palette">
    <h3 class="abs heading-md" style="left:137px; top:68px;">Primary</h3>
    <span class="swatch" style="left:137px; background:var(--primary-dark);"></span>
    <span class="swatch" style="left:163px; background:var(--primary);"></span>
    <span class="swatch" style="left:195px; background:var(--primary-light);"></span>

    <h3 class="abs heading-md" style="left:375px; top:68px;">Secondary</h3>
    <span class="swatch" style="left:376px; background:var(--secondary);"></span>
    <span class="swatch" style="left:400px; background:var(--secondary-light);"></span>

    <h3 class="abs heading-md" style="left:612px; top:68px;">Accent</h3>
    <span class="swatch" style="left:612px; background:var(--accent);"></span>
    <span class="swatch" style="left:637px; background:var(--accent-light);"></span>

    <h3 class="abs heading-md" style="left:851px; top:68px;">Dark Tones</h3>
    <span class="swatch" style="left:851px; background:var(--tone-charcoal);"></span>
    <span class="swatch" style="left:876px; background:var(--tone-slate);"></span>
  </section>

  <!-- Buttons -->
  <h2 class="abs heading-xl" style="left:137px; top:179px;">Buttons</h2>

  <h3 class="abs heading-md" style="left:137px; top:256px;">Primary Button</h3>
  <div class="btn btn-icon solid-primary" style="left:137px; top:283px;"><svg width="12" height="12"><use href="#heart"/></svg>Icon button</div>
  <div class="btn btn-icon solid-secondary" style="left:323px; top:283px;"><svg width="12" height="12"><use href="#heart"/></svg>Icon button</div>
  <div class="btn btn-icon solid-accent" style="left:507px; top:283px;"><svg width="12" height="12"><use href="#heart"/></svg>Icon button</div>

  <div class="btn btn-chevron solid-primary" style="left:137px; top:321px;">Large button<svg width="11" height="13"><use href="#chevron"/></svg></div>
  <div class="btn btn-chevron solid-secondary" style="left:323px; top:321px;">Large button<svg width="11" height="13"><use href="#chevron"/></svg></div>
  <div class="btn btn-chevron solid-accent" style="left:507px; top:321px;">Large button<svg width="11" height="13"><use href="#chevron"/></svg></div>

  <div class="btn btn-large solid-primary" style="left:137px; top:368px;">Large button</div>
  <div class="btn btn-large solid-secondary" style="left:323px; top:368px;">Large button</div>
  <div class="btn btn-large solid-accent" style="left:507px; top:368px;">Large button</div>

  <h3 class="abs heading-md" style="left:137px; top:451px;">Second Button</h3>
  <div class="btn btn-icon outline-primary" style="left:137px; top:477px;"><svg width="12" height="12"><use href="#heart"/></svg>Icon button</div>
  <div class="btn btn-icon outline-secondary" style="left:323px; top:477px;"><svg width="12" height="12"><use href="#heart"/></svg>Icon button</div>
  <div class="btn btn-icon outline-accent" style="left:507px; top:477px;"><svg width="12" height="12"><use href="#heart"/></svg>Icon button</div>

  <div class="btn btn-chevron outline-primary" style="left:137px; top:516px;">Large button<svg width="11" height="13"><use href="#chevron"/></svg></div>
  <div class="btn btn-chevron outline-secondary" style="left:323px; top:516px;">Large button<svg width="11" height="13"><use href="#chevron"/></svg></div>
  <div class="btn btn-chevron outline-accent" style="left:507px; top:516px;">Large button<svg width="11" height="13"><use href="#chevron"/></svg></div>

  <div class="btn btn-large outline-primary" style="left:137px; top:563px;">Large button</div>
  <div class="btn btn-large outline-secondary" style="left:323px; top:563px;">Large button</div>
  <div class="btn btn-large outline-accent" style="left:507px; top:563px;">Large button</div>

  <h3 class="abs heading-md" style="left:137px; top:646px;">Text Button</h3>
  <div class="text-btn text-primary" style="left:137px; top:677px;"><svg width="12" height="12"><use href="#heart"/></svg>Icon button</div>
  <div class="text-btn text-primary" style="left:137px; top:697px;">Large button<svg width="8" height="10"><use href="#chevron"/></svg></div>
  <div class="text-btn text-primary" style="left:137px; top:717px;">Large button</div>

  <div class="text-btn text-secondary" style="left:276px; top:677px;"><svg width="12" height="12"><use href="#heart"/></svg>Icon button</div>
  <div class="text-btn text-secondary" style="left:276px; top:697px;">Large button<svg width="8" height="10"><use href="#chevron"/></svg></div>
  <div class="text-btn text-secondary" style="left:276px; top:717px;">Large button</div>

  <div class="text-btn text-accent" style="left:415px; top:677px;"><svg width="12" height="12"><use href="#heart"/></svg>Icon button</div>
  <div class="text-btn text-accent" style="left:415px; top:697px;">Large button<svg width="8" height="10"><use href="#chevron"/></svg></div>
  <div class="text-btn text-accent" style="left:415px; top:717px;">Large button</div>

  <h3 class="abs heading-md" style="left:137px; top:776px;">Button Group</h3>
  <div class="group-btn solid-primary" style="left:137px; width:66px;">Primary</div>
  <div class="group-btn outline-primary" style="left:215px; width:82px;">Secondary</div>

  <h3 class="abs heading-md" style="left:612px; top:776px;">Icon only</h3>
  <div class="icon-round" style="left:612px;"><svg width="13" height="15" fill="#fff"><use href="#chevron"/></svg></div>
  <div class="icon-round" style="left:649px;"><svg width="18" height="18" viewBox="0 0 24 24" fill="none" stroke="#fff" stroke-width="3.5" stroke-linecap="round" stroke-linejoin="round"><path d="M4 12h15M13 5l7 7-7 7"/></svg></div>
  <div class="icon-round" style="left:687px;"><svg width="14" height="14" viewBox="0 0 24 24" fill="none" stroke="#fff" stroke-width="5" stroke-linecap="round"><path d="M5 5l14 14M19 5 5 19"/></svg></div>
  <div class="chip">Tacos<svg width="10" height="10" viewBox="0 0 24 24" fill="none" stroke="#fff" stroke-width="5" stroke-linecap="round"><path d="M5 5l14 14M19 5 5 19"/></svg></div>

  <h3 class="abs heading-md" style="left:137px; top:880px;">Radio Button</h3>
  <div class="form-row" style="top:910px;"><span class="radio on"></span>Radio</div>
  <div class="form-row" style="top:930px;"><span class="radio off"></span>Radio</div>
  <div class="form-row" style="top:950px;"><span class="checkbox"><svg width="9" height="9" viewBox="0 0 24 24" fill="none" stroke="#fff" stroke-width="4" stroke-linecap="round" stroke-linejoin="round"><path d="M4 12l5 5L20 6"/></svg></span>Checkbox</div>
  <div class="form-row" style="top:970px; left:137px;">Toggle</div>
  <div class="toggle"></div>
</body>
</html>
```